Stationary Package for Construction Company
Harborline Construction & Development, LLC
Stationary Package for Construction Company - Construction
Creative Brief
Bright & Fun-filled
Kevin R. Tolliver
Partner
1587 Marlow Avenue, STE 210 Myrtle Beach, SC 29577
kevin@harborlinehomebuilders.example
www.harborlinehomebuilders.example
travelkq travelkq

```html
<!DOCTYPE html>
<html lang="en">
<head>
<meta charset="utf-8">
<title>Harborline Construction &amp; Development — Business Cards</title>
<link href="https://fonts.googleapis.com/css2?family=Montserrat:wght@400;500;600;700&display=swap" rel="stylesheet">
<style>
  :root {
    --bg: #1d1d1f;
    --card-dark: #111112;
    --card-light: #ffffff;
    --red: #e0262b;
    --ink: #1a1a1a;
    --muted: #6b6b6b;
    --white: #ffffff;
  }
  * { box-sizing: border-box; margin: 0; padding: 0; }
  html, body { width: 1200px; height: 901px; overflow: hidden; }
  body {
    background: var(--bg);
    font-family: "Montserrat", Arial, sans-serif;
    position: relative;
  }
  .card {
    position: absolute;
    width: 490px;
    height: 280px;
    box-shadow: 0 18px 40px rgba(0,0,0,.55);
  }
  .card--back { left: 90px; top: 170px; background: var(--card-dark); }
  .card--front { left: 620px; top: 450px; background: var(--card-light); }

  .brand { display: flex; align-items: center; gap: 12px; }
  .brand__mark { width: 34px; height: 34px; border-radius: 50%; background: var(--red); flex: none; }
  .brand__name { font-weight: 600; font-size: 30px; letter-spacing: 5px; line-height: 1; }
  .brand__tagline { font-size: 8.5px; letter-spacing: 1.6px; color: var(--red); margin-top: 5px; text-transform: uppercase; }

  .card--back .brand { position: absolute; left: 112px; top: 104px; }
  .card--back .brand__name { color: var(--white); }
  .card--back .website {
    position: absolute; left: 30px; bottom: 26px;
    color: var(--white); font-size: 10px; letter-spacing: .5px;
  }

  .card--front .brand { position: absolute; right: 28px; top: 32px; }
  .card--front .brand__mark { width: 28px; height: 28px; }
  .card--front .brand__name { color: var(--ink); font-size: 24px; letter-spacing: 4px; }
  .card--front .brand__tagline { font-size: 7px; }

  .person { position: absolute; left: 28px; top: 104px; }
  .person__name { color: var(--red); font-weight: 700; font-size: 15px; letter-spacing: 1px; text-transform: uppercase; }
  .person__title { color: var(--muted); font-size: 10px; margin-top: 3px; }

  .rule { position: absolute; left: 28px; right: 28px; height: 1.5px; background: var(--red); }
  .rule--top { top: 150px; }
  .rule--bottom { bottom: 22px; }

  .contact { position: absolute; left: 28px; top: 166px; list-style: none; }
  .contact li { display: flex; align-items: center; gap: 8px; font-size: 9.5px; color: var(--ink); margin-bottom: 6px; }
  .contact svg { width: 10px; height: 10px; fill: var(--red); flex: none; }

  .address { position: absolute; right: 28px; top: 172px; text-align: right; font-size: 9.5px; line-height: 1.55; color: var(--ink); font-style: normal; }
  .address .web { color: var(--red); }
</style>
</head>
<body>
  <section class="card card--back" aria-label="Card back">
    <div class="brand">
      <span class="brand__mark"></span>
      <div>
        <div class="brand__name">HARBORLINE</div>
        <div class="brand__tagline">Construction &amp; Development, LLC</div>
      </div>
    </div>
    <p class="website">www.harborlinehomebuilders.example</p>
  </section>

  <section class="card card--front" aria-label="Card front">
    <div class="brand">
      <span class="brand__mark"></span>
      <div>
        <div class="brand__name">HARBORLINE</div>
        <div class="brand__tagline">Construction &amp; Development, LLC</div>
      </div>
    </div>

    <div class="person">
      <h1 class="person__name">Kevin R. Tolliver</h1>
      <p class="person__title">Partner</p>
    </div>

    <div class="rule rule--top"></div>

    <ul class="contact">
      <li><svg viewBox="0 0 10 10"><path d="M2 0h2l1 3-1.5 1a6 6 0 0 0 2.5 2.5L7 5l3 1v2a2 2 0 0 1-2 2A8 8 0 0 1 0 2a2 2 0 0 1 2-2z"/></svg>843-555-0142</li>
      <li><svg viewBox="0 0 10 10"><rect x="1" y="0" width="8" height="10" rx="1.5"/></svg>843-555-0187</li>
      <li><svg viewBox="0 0 10 10"><rect x="0" y="3" width="10" height="6"/><rect x="2" y="0" width="6" height="3"/></svg>843-555-0119</li>
      <li><svg viewBox="0 0 10 10"><path d="M0 2h10v6H0z M0 2l5 3.5L10 2" /></svg>kevin@harborlinehomebuilders.example</li>
    </ul>

    <address class="address">
      1587 Marlow Avenue, STE 210<br>
      Myrtle Beach, SC 29577<br>
      <span class="web">www.harborlinehomebuilders.example</span>
    </address>

    <div class="rule rule--bottom"></div>
  </section>
</body>
</html>
```